Flyer Design

I'm looking for a new flyer design to help promote our landscape company, and some of our main service for the up and coming season. We're trying to position ourselves as a leader in our market, so obviously quality is important to us.

Our current promotion is 25% off the first month with signup of annual service.

Phone Number: (816) 555-0193
Website: gardelvista.com
Our tagline: "Your hands are full... Let us help"

The call to action: direct them to our website for a detailed list of services and to receive a free quote.

You're welcome to add your own wording and punctuation. If I like the design I will provide feedback accordingly.

I have attached a jpg of our logo to help with design colors. I will provide the vector file upon completion of this project.

Also, I've attached a few photos that I had on hand of our companies work that may help with the design. Obviously I don't want to use them all, but there are a couple just to help out. I'm not opposed to stock photos either.
Thanks

Target Market(s)

We market to high end customers, generally with home between $500k-$2mil, or household income over $200k. Quality and creativity are most important to us.

Industry/Entity Type

Landscape

Requirements
Must have
• Creativity, easy to read, modern style.

```html
<!DOCTYPE html>
<html lang="en">
<head>
<meta charset="utf-8">
<title>Gardel Vista – Lawn Service Flyer</title>
<link rel="stylesheet" href="https://fonts.googleapis.com/css2?family=Barlow:wght@600;700&family=Graduate&family=Libre+Baskerville:wght@400;700&display=swap">
<style>
  :root {
    --sage: #6c968a;
    --mint: #a9cfc0;
    --pale-mint: #d8f0c8;
    --sun: #fde400;
    --gold: #f7c600;
    --ink: #0b0b0b;
    --white: #ffffff;
    --red: #e23b2e;
  }
  html, body { margin: 0; padding: 0; overflow: hidden; }
  body { width: 923px; height: 1200px; background: var(--sage); }
  .flyer {
    position: relative;
    width: 923px;
    height: 1200px;
    overflow: hidden;
    background: var(--sage);
    font-family: "Barlow", Arial, sans-serif;
  }
  .backdrop { position: absolute; inset: 0; }

  .offer-amount {
    position: absolute;
    left: 72px;
    top: 28px;
    margin: 0;
    font-family: "Barlow", Arial, sans-serif;
    font-weight: 700;
    font-size: 150px;
    line-height: 186px;
    color: var(--mint);
    letter-spacing: 2px;
  }
  .offer-terms {
    position: absolute;
    left: 420px;
    top: 46px;
    margin: 0;
    width: 110px;
    font-weight: 600;
    font-size: 28px;
    line-height: 39px;
    color: var(--white);
  }

  .brand {
    position: absolute;
    left: 610px;
    top: 96px;
    display: flex;
    align-items: center;
    gap: 12px;
  }
  .brand-dot {
    width: 26px; height: 26px;
    border-radius: 50%;
    background: var(--red);
  }
  .brand-name {
    font-family: "Graduate", Georgia, serif;
    font-size: 30px;
    color: var(--ink);
    letter-spacing: 1px;
  }

  .tagline {
    position: absolute;
    left: 562px;
    top: 270px;
    margin: 0;
    font-family: "Graduate", Georgia, serif;
    font-weight: 400;
    font-size: 72px;
    line-height: 98px;
    letter-spacing: 2px;
  }
  .tagline .dark { color: var(--ink); display: block; }
  .tagline .light { color: var(--white); display: block; }

  .quote-cta {
    position: absolute;
    left: 68px;
    top: 424px;
    margin: 0;
    font-family: "Graduate", Georgia, serif;
    font-size: 32px;
    line-height: 43px;
    color: var(--gold);
    letter-spacing: 1px;
  }

  .services-title {
    position: absolute;
    left: 66px;
    top: 608px;
    margin: 0;
    font-family: "Libre Baskerville", Georgia, serif;
    font-weight: 400;
    font-size: 42px;
    color: var(--white);
  }
  .services-list {
    position: absolute;
    left: 68px;
    top: 690px;
    margin: 0;
    padding: 0;
    list-style: none;
  }
  .services-list li {
    position: relative;
    padding-left: 30px;
    font-family: "Libre Baskerville", Georgia, serif;
    font-weight: 700;
    font-size: 23px;
    line-height: 38px;
    color: var(--pale-mint);
  }
  .services-list li::before {
    content: "";
    position: absolute;
    left: 0;
    top: 12px;
    width: 10px; height: 10px;
    background: var(--gold);
  }

  .contact {
    position: absolute;
    left: 624px;
    top: 1090px;
    margin: 0;
    font-weight: 700;
    font-size: 23px;
    line-height: 29px;
    color: var(--white);
  }
  .contact-row { display: flex; align-items: center; gap: 8px; }
  .contact-row svg { flex: none; }
</style>
</head>
<body>
<main class="flyer">
  <svg class="backdrop" width="923" height="1200" viewBox="0 0 923 1200" aria-hidden="true">
    <defs>
      <radialGradient id="beadGlow" cx="50%" cy="60%" r="65%">
        <stop offset="0" stop-color="#f7c600" stop-opacity="0.9"/>
        <stop offset="1" stop-color="#f7c600" stop-opacity="0.25"/>
      </radialGradient>
    </defs>
    <circle cx="754" cy="150" r="246" fill="var(--sun)"/>
    <rect x="0" y="554" width="923" height="646" fill="var(--ink)"/>
    <path d="M0,1130 Q280,1070 560,1080 T923,1010 L923,1200 L0,1200 Z" fill="var(--sage)"/>
    <g fill="none" stroke="var(--gold)" stroke-width="6" stroke-dasharray="22 12">
      <polyline points="328,506 538,506 538,246 903,246 903,877 472,877 565,1138"/>
    </g>
    <polygon points="580,1128 580,1150 598,1139" fill="var(--gold)"/>
  </svg>

  <svg style="position:absolute;left:0;top:900px" width="923" height="250" viewBox="0 0 923 250" role="img" aria-label="Decorative chain of yellow beads and pins across the lower band">
    <path d="M0,60 Q300,-10 923,70 L923,170 Q600,200 470,215 Q200,250 0,190 Z" fill="url(#beadGlow)" opacity="0.85"/>
  </svg>

  <h1 class="offer-amount">25%<br>OFF</h1>
  <p class="offer-terms">For the first month, When you sign up for weekly lawn</p>

  <div class="brand">
    <span class="brand-dot"></span>
    <span class="brand-name">GARDEL VISTA</span>
  </div>

  <h2 class="tagline">
    <span class="dark">YOUR</span>
    <span class="dark">HANDS</span>
    <span class="dark">ARE</span>
    <span class="light">FULL...</span>
    <span class="light">LET US</span>
    <span class="light">HELP</span>
  </h2>

  <p class="quote-cta">TO RECEIVE<br>A FREE<br>QUOTE</p>
  <svg style="position:absolute;left:218px;top:477px" width="58" height="92" viewBox="0 0 58 92" aria-hidden="true">
    <path d="M2,0 H56 V48 Q50,78 18,92 L14,84 Q30,72 30,58 H2 Z" fill="var(--gold)"/>
  </svg>

  <h3 class="services-title">OUR SERVICES</h3>
  <ul class="services-list">
    <li>MOWING</li>
    <li>BRUSH &amp; TREE TRIMMING</li>
    <li>INSECT MANAGEMENT</li>
    <li>SNOW REMOVAL</li>
    <li>ICE TREATMENT</li>
    <li>AREATION SERVICES</li>
  </ul>

  <address class="contact">
    <span class="contact-row">
      <svg width="16" height="24" viewBox="0 0 16 24" aria-hidden="true"><rect x="2" y="1" width="12" height="22" rx="2" fill="none" stroke="#fff" stroke-width="2"/><rect x="5" y="4" width="6" height="7" fill="#fff"/></svg>
      (816) 555-0193
    </span>
    <span class="contact-row">
      <svg width="20" height="18" viewBox="0 0 20 18" aria-hidden="true"><rect x="1" y="1" width="18" height="12" rx="1" fill="none" stroke="#fff" stroke-width="2"/><rect x="7" y="14" width="6" height="3" fill="#fff"/><rect x="4" y="4" width="5" height="3" fill="#fff"/><rect x="11" y="4" width="5" height="1.5" fill="#fff"/><rect x="11" y="7" width="5" height="1.5" fill="#fff"/></svg>
      gardelvista.com
    </span>
  </address>
</main>
</body>
</html>
```